Elegant wine label

Looking for a new Napa Valley wine label called "Velmora". Our wines will retail for $150 + per bottle. Velmora is derived from the greek word Ergo (therefore) tied in with Air for aeration for wine.

We handcraft our small production wine. 200 cases.
Looking for a very sophisticated, minimalist elegant look. Wine labels we like for inspiration and reference include: www.tarvik.wine, www.pellunwine.com, www.morvadestates.com, www.quillbarrowwine.com, www.brevixestate.com/Wine, https://shop.lantivewine.com/wine

Colors will include white, black and blue foil (Approx. color: C 94.9, M 83.53, Y 0, K 0). We want a custom-created, minimal greek/roman looking font for lettering.

```html
<!DOCTYPE html>
<html lang="en">
<head>
<meta charset="utf-8">
<title>Velmora — Napa Valley Wine Label</title>
<link rel="stylesheet" href="https://fonts.googleapis.com/css2?family=Cormorant+Garamond:ital,wght@0,400;1,400&display=swap">
<style>
  :root {
    --backdrop: #9a9592;
    --paper: #c8dde2;
    --paper-light: #d4e6ea;
    --foil-blue: #1f3fd8;
    --foil-bright: #2f7fe8;
    --rule-grey: #a9b4b7;
    --mark-blue: #2aa6d9;
    --ink: #2b2b2b;
  }
  * { box-sizing: border-box; margin: 0; padding: 0; }
  html, body {
    width: 1200px;
    height: 1200px;
    overflow: hidden;
    background: var(--backdrop);
  }
  .canvas {
    position: relative;
    width: 1200px;
    height: 1200px;
    display: flex;
    align-items: center;
    justify-content: center;
  }
  .label {
    position: relative;
    width: 760px;
    height: 900px;
    background: radial-gradient(ellipse at 40% 35%, var(--paper-light), var(--paper) 70%);
    box-shadow: 0 10px 30px rgba(0,0,0,0.25);
  }
  .label-frame {
    position: absolute;
    inset: 0;
    width: 100%;
    height: 100%;
  }
  .wordmark {
    position: absolute;
    top: 260px;
    left: 0;
    right: 0;
    text-align: center;
    font-family: "Cormorant Garamond", serif;
    font-weight: 400;
    font-size: 150px;
    line-height: 1;
    letter-spacing: 4px;
    color: var(--mark-blue);
  }
  .appellation {
    position: absolute;
    top: 700px;
    left: 0;
    right: 0;
    text-align: center;
    font-family: "Cormorant Garamond", serif;
    font-style: italic;
    font-weight: 400;
    font-size: 28px;
    letter-spacing: 14px;
    color: var(--ink);
  }
  .appellation .gap { display: inline-block; width: 28px; }
</style>
</head>
<body>
  <main class="canvas">
    <article class="label">
      <svg class="label-frame" viewBox="0 0 760 900" aria-hidden="true">
        <polygon class="frame-foil" points="40,40 720,40 720,150 760,190 760,900" fill="none" stroke="none"/>
        <polygon points="30,30 640,30 730,120 730,780 640,870 30,870"
                 fill="none" stroke="var(--foil-blue)" stroke-width="7"/>
        <polygon points="48,48 632,48 712,128 712,772 632,852 48,852"
                 fill="none" stroke="var(--rule-grey)" stroke-width="3"/>
      </svg>
      <h1 class="wordmark">Velmora</h1>
      <p class="appellation">NAPA<span class="gap"></span>VALLEY<span class="gap"></span>WINE</p>
    </article>
  </main>
</body>
</html>
```